Redesign trade show stand graphics for Harbourline Panels

Update existing graphics of a trade show stand consisting of 2 walls. See the current design attached.

Left wall size is 2.4m high x 2700mm wide (made up of 3 pieces of 2400mm high x 900mm wide). The artwork will be printed on self adhesive stickers to cover the 2 walls.

NEW DESIGN LEFT WALL (2.4m high x 3m wide)
Headline at the top of the wall should read:
RENOVATE YOUR KITCHEN
the quick, easy and cost effective way:
JUST REPLACE THE DOORS and panels
• Cost effective: Save $$$
• Quick: approx. 15 working days
• Easy: No mess or inconvenience
• Polyurethane finish, unlimited choice of colours
• Measure, quote and install - DIY or contact our installers
• Delivery Australia wide
Harbourline Panels logo at top of left and right walls. See logo attached. “Australian made” logo somewhere on the wall (logo attached)
The main body of the left wall will contain a “before” and “after” photo of a kitchen. Size of “before” shot approximately 250mm wide x 150mm high and “after” shot approximately 1m wide x 600mm high. Photo with higher resolution will be supplied.
Text:
• We replace doors, panels, drawer fronts and kickboards - all painted in polyurethane.
• We drill doors for new or existing hinges. We supply Vorn soft closing hinges, door handles, wardrobe door tracks and decorative items such as corbels, flutes and rosettes and capping.
• Our installers measure, quote and install or save money and do it yourself - DIY
Headline under the above: UPDATE YOUR BUILT IN WARDROBES WITH NEW DOORS
Sub headline: Custom made to your sizes and painted in polyurethane in the colour of your choice
2 photos of wardrobes to go under this headline

NEW DESIGN RIGHT WALL (2.4m high x 2800mm wide made up of 1 x 1000mm piece and 2 x 900mm pieces)
Visit our website: harbourlinepanels.com.au
Headline: SAVE TIME AND MONEY – REPLACE YOUR OLD DOORS (and panels)
Sub headline: WITH ONES PAINTED IN POLYURETHANE
Sub sub headline:
TO GET A QUOTE:
• DIY measure doors and panels and fill in our Quote Form or
• Contact our installers to measure, quote and install

At 1.5m high: 2 rows of 7 rectangular outlines 400mm high x 300mm wide (for sample doors that will be hung on the wall).
Directly under that, another headline:
Many more designs in our showroom at
47 Kestrel Avenue, Marlow Heights NSW 2837
Phone: (02) 9318 6072
Email: sales@harbourlinepanels.com.au
Website: harbourlinepanels.com.au
Place image of our showroom (attached) to the left or right.

“Australian made” logo and "Trade and public welcome" logo somewhere on the wall (logos attached).
Small listing of approximately A5 size of “What we do”, “What we don’t do” and “What you do”. These will be supplied in bullet points.
Another image to use is uploaded below.

Target Market(s)

Home owners, home renovators

Industry/Entity Type

Trade

Font styles to use
Sans Serif
Other font styles liked:
• A font similar to that used on our website www.harbourlinepanels.com.au

Colors
f8972e

Requirements
Must have
• The background colour of the stand artwork should remain the same bright colour of our logo. The fonts should be similar to that used on our website www.harbourlinepanels.com.au
Nice to have
• Fun and engaging design

```html
<!DOCTYPE html>
<html lang="en">
<head>
<meta charset="utf-8">
<title>Harbourline Panels – Stand Walls</title>
<link rel="stylesheet" href="https://fonts.googleapis.com/css2?family=Source+Sans+3:wght@400;600;700&family=Roboto+Condensed:wght@700&display=swap">
<style>
:root{
  --stage:#3a3a3c;
  --orange:#f8972e;
  --orange-deep:#ef6a2c;
  --orange-light:#f5a94a;
  --red:#b3212b;
  --grey:#808083;
  --grey-light:#d5d6d8;
  --ink:#3b3b3b;
  --white:#ffffff;
}
*{margin:0;padding:0;box-sizing:border-box}
html,body{width:1200px;height:582px;overflow:hidden;background:var(--stage);font-family:"Source Sans 3",Arial,sans-serif}
.stage{position:relative;width:1200px;height:582px}
.wall{position:absolute;top:92px;height:404px;background:var(--white);overflow:hidden;box-shadow:0 6px 10px rgba(0,0,0,.45)}
.wall--left{left:94px;width:454px}
.wall--right{left:638px;width:470px}
.abs{position:absolute}
.photo{position:absolute;background:linear-gradient(135deg,#e9e6e2,#b9b2aa)}
.diamond{position:absolute;transform:rotate(45deg)}
.diamond--orange{background:var(--orange-deep)}
.diamond--amber{background:var(--orange)}
.diamond--white{background:var(--white);box-shadow:0 0 4px rgba(0,0,0,.15)}
.brand{position:absolute;display:flex;align-items:center;gap:5px;font-family:"Source Sans 3",sans-serif;font-weight:700;color:var(--ink);line-height:1.05}
.brand__mark{width:12px;height:12px;background:var(--orange)}
/* left wall */
.headline{position:absolute;right:6px;top:24px;width:300px;text-align:center;color:var(--red);font-weight:700;font-size:25px;line-height:30px;white-space:nowrap}
.tagline{position:absolute;right:6px;top:55px;width:300px;text-align:center;color:#555;font-size:13px;white-space:nowrap}
.tagline--strong{top:70px;font-size:15.5px}
.tagline--strong b{color:var(--orange);font-weight:700}
.benefits{position:absolute;left:134px;top:106px;width:320px;height:111px;background:var(--grey);clip-path:polygon(28% 0,100% 0,100% 100%,0 100%)}
.benefits ul{position:absolute;left:80px;top:10px;list-style:none;color:var(--white);font-size:10px;line-height:15px;white-space:nowrap}
.shot{position:absolute;border:3px solid var(--white);box-shadow:0 2px 4px rgba(0,0,0,.3)}
.shot--before{left:192px;top:234px;width:107px;height:70px;background:linear-gradient(135deg,#8a5a34,#5b3a22)}
.shot--after{left:318px;top:230px;width:125px;height:85px;background:linear-gradient(135deg,#ddd8d0,#9e958b)}
.shot__label{position:absolute;left:-3px;bottom:-3px;background:var(--orange);color:var(--white);font-size:7px;font-weight:700;padding:3px 6px}
.services{position:absolute;left:0;top:330px;width:454px;height:74px;background:var(--grey-light)}
.services__text{position:absolute;left:9px;top:17px;width:262px;font-size:7px;line-height:10.4px;color:var(--ink)}
.diy{position:absolute;left:270px;top:326px;width:184px;height:78px;background:var(--orange-deep);clip-path:polygon(9% 0,100% 0,100% 100%,0 100%)}
.diy__text{position:absolute;left:22px;top:8px;width:160px;color:var(--white);font-size:9px;line-height:12.5px}
.badge{position:absolute;left:24px;top:52px;width:42px;height:16px;background:var(--orange-light);border-radius:2px}
.welcome{position:absolute;left:80px;top:53px;font-family:"Roboto Condensed",sans-serif;font-weight:700;font-size:6.4px;line-height:7.6px;color:#111;white-space:nowrap}
/* right wall */
.title{position:absolute;left:0;top:13px;width:470px;text-align:center;color:var(--orange-deep);font-weight:700;font-size:18px;line-height:22px;white-space:nowrap}
.subtitle{position:absolute;left:0;top:36px;width:470px;text-align:center;color:var(--ink);font-size:11.5px;white-space:nowrap}
.sample-band{position:absolute;left:0;top:56px;width:470px;height:162px;background:var(--orange)}
.sample-slot{position:absolute;width:50px;height:67px;border:1px solid var(--white)}
.quote-band{position:absolute;left:0;top:228px;width:470px;height:68px;background:var(--grey)}
.quote-title{position:absolute;left:110px;top:234px;width:280px;text-align:center;color:var(--white);font-weight:700;font-size:14px}
.quote-list{position:absolute;left:116px;top:254px;list-style:none;color:var(--white);font-size:10px;line-height:13px;white-space:nowrap}
.save{position:absolute;left:392px;top:242px;width:68px;height:68px;border-radius:50%;background:var(--orange-deep);color:var(--white);font-weight:700;font-size:11px;line-height:13px;display:flex;align-items:center;justify-content:center;text-align:center}
.showroom{position:absolute;left:0;top:361px;width:470px;text-align:center;color:var(--orange-deep);font-weight:700;font-size:9px;white-space:nowrap}
.contact-bar{position:absolute;left:0;top:378px;width:470px;height:26px;background:var(--orange);display:flex;align-items:center;justify-content:space-around;color:var(--white);font-size:11px}
.contact-bar span{display:flex;align-items:center;gap:6px}
.contact-bar svg{width:11px;height:11px}
</style>
</head>
<body>
<main class="stage">

  <section class="wall wall--left">
    <div class="photo" role="img" aria-label="White gloss kitchen cabinets with oven and pepper mills" style="left:0;top:0;width:170px;height:330px"></div>
    <div class="abs" style="left:110px;top:0;width:140px;height:120px;background:var(--white);clip-path:polygon(60% 0,100% 0,100% 100%,0 100%)"></div>
    <div class="diamond diamond--amber" style="left:103px;top:-12px;width:40px;height:40px;opacity:.8"></div>
    <div class="diamond diamond--amber" style="left:80px;top:28px;width:46px;height:46px"></div>
    <div class="diamond diamond--orange" style="left:8px;top:152px;width:38px;height:38px;opacity:.85"></div>
    <div class="diamond diamond--orange" style="left:32px;top:180px;width:40px;height:40px"></div>
    <div class="diamond diamond--amber" style="left:75px;top:224px;width:40px;height:40px;opacity:.85"></div>
    <div class="diamond diamond--orange" style="left:40px;top:248px;width:38px;height:38px"></div>
    <div class="diamond diamond--orange" style="left:152px;top:220px;width:38px;height:38px"></div>
    <div class="diamond diamond--white" style="left:58px;top:86px;width:124px;height:124px"></div>
    <div class="brand" style="left:82px;top:134px;font-size:15px"><i class="brand__mark"></i>Harbourline<br>Panels</div>

    <h1 class="headline">RENOVATE YOUR KITCHEN</h1>
    <p class="tagline">the quick, easy and cost effective way:</p>
    <p class="tagline tagline--strong"><b>JUST REPLACE THE DOORS</b> and panels</p>

    <div class="benefits">
      <ul>
        <li>• Cost effective: Save $$$</li>
        <li>• Quick: approx. 15 working days</li>
        <li>• Easy: No mess or inconvenience</li>
        <li>• Polyurethane finish, unlimited choice of colours</li>
        <li>• Measure, quote and install - DIY or contact our installers</li>
        <li>• Delivery Australia wide</li>
      </ul>
    </div>

    <div class="shot shot--before" role="img" aria-label="Kitchen before: dark timber cabinet doors"><span class="shot__label">BEFORE</span></div>
    <div class="shot shot--after" role="img" aria-label="Kitchen after: white painted cabinet doors"><span class="shot__label">AFTER</span></div>

    <div class="services">
      <p class="services__text">We replace doors, panels, drawer fronts and kickboards - all painted in polyurethane. &nbsp;We drill doors for new or existing hinges. We supply Vorn soft closing hinges, door handles, wardrobe door tracks and decorative items such as corbels, flutes and rosettes and capping.</p>
    </div>
    <div class="diy">
      <p class="diy__text">Our installers measure, quote and install or save money and do it yourself - DIY</p>
      <div class="badge" role="img" aria-label="Local manufacturing badge"></div>
      <div class="welcome">TRADE AND GENERAL<br>PUBLIC ENQUIRIES WELCOME</div>
    </div>
  </section>

  <section class="wall wall--right">
    <h2 class="title">UPDATE YOUR KITCHEN AND WARDROBES WITH NEW DOORS</h2>
    <p class="subtitle">Custom made to your sizes and painted in polyurethane in the colour of your choice</p>

    <div class="sample-band">
      <div class="sample-slot" style="left:44px;top:14px"></div>
      <div class="sample-slot" style="left:100px;top:14px"></div>
      <div class="sample-slot" style="left:155px;top:14px"></div>
      <div class="sample-slot" style="left:211px;top:14px"></div>
      <div class="sample-slot" style="left:266px;top:14px"></div>
      <div class="sample-slot" style="left:322px;top:14px"></div>
      <div class="sample-slot" style="left:377px;top:14px"></div>
      <div class="sample-slot" style="left:44px;top:86px"></div>
      <div class="sample-slot" style="left:100px;top:86px"></div>
      <div class="sample-slot" style="left:155px;top:86px"></div>
      <div class="sample-slot" style="left:211px;top:86px"></div>
      <div class="sample-slot" style="left:266px;top:86px"></div>
      <div class="sample-slot" style="left:322px;top:86px"></div>
      <div class="sample-slot" style="left:377px;top:86px"></div>
    </div>

    <div class="quote-band"></div>
    <div class="diamond diamond--amber" style="left:-10px;top:318px;width:34px;height:34px"></div>
    <div class="diamond diamond--orange" style="left:54px;top:300px;width:34px;height:34px"></div>
    <div class="diamond diamond--white" style="left:-12px;top:230px;width:106px;height:106px"></div>
    <div class="brand" style="left:4px;top:270px;font-size:13px"><i class="brand__mark"></i>Harbourline<br>Panels</div>

    <h3 class="quote-title">TO GET A QUOTE:</h3>
    <ul class="quote-list">
      <li>• DIY measure doors and panels and fill in our Quote Form or</li>
      <li>• Contact our installers to measure, quote and install</li>
    </ul>

    <div class="shot" role="img" aria-label="Bedroom with white built-in wardrobe doors" style="left:93px;top:289px;width:102px;height:62px;background:linear-gradient(135deg,#f1f0ee,#c7c3bd)"></div>
    <div class="shot" role="img" aria-label="Showroom with floor-to-ceiling wardrobe doors" style="left:212px;top:289px;width:102px;height:62px;background:linear-gradient(135deg,#d8d2c7,#6f6a64)"></div>
    <div class="shot" role="img" aria-label="Bright kitchen with white island and bar stools" style="left:330px;top:289px;width:112px;height:62px;background:linear-gradient(135deg,#f3f1ee,#a9a29a)"></div>

    <div class="save">SAVE<br>TIME AND<br>MONEY</div>

    <p class="showroom">Many more designs in our showroom at: 47 Kestrel Avenue, Marlow Heights NSW 2837</p>

    <div class="contact-bar">
      <span><svg viewBox="0 0 12 12"><rect x="0" y="0" width="12" height="12" rx="2" fill="#ef6a2c"/><path d="M2.5 4h7v4.5h-7z M2.5 4l3.5 2.6L9.5 4" fill="none" stroke="#fff" stroke-width="1"/></svg>sales@harbourlinepanels.com.au</span>
      <span><svg viewBox="0 0 12 12"><rect x="0" y="0" width="12" height="12" rx="2" fill="#ef6a2c"/><path d="M4 3l1.3 1.8-.8.9a5 5 0 0 0 1.9 1.9l.9-.8L9 8 8 9.2C5.6 9 3 6.4 2.8 4z" fill="#fff"/></svg>(02) 9318 6072</span>
      <span><svg viewBox="0 0 12 12"><rect x="0" y="0" width="12" height="12" rx="2" fill="#ef6a2c"/><circle cx="6" cy="6" r="3.3" fill="none" stroke="#fff" stroke-width="1"/><path d="M2.7 6h6.6M6 2.7c-1.6 2-1.6 4.6 0 6.6M6 2.7c1.6 2 1.6 4.6 0 6.6" fill="none" stroke="#fff" stroke-width=".8"/></svg>harbourlinepanels.com.au</span>
    </div>
  </section>

</main>
</body>
</html>
```